Window and GutterCleaning Flyer A5 size double sided.

We need a double sided A5 flyer. Side 1, is for window cleaning, side 2 is for gutter cleaning. Licensed by Borough of Halvern Council.
Phone number 0800 315 4720.
Business address 7 Tarnlow Brae, North Pellin Edinburgh EH14 3RW.
www.clearpane-vista-services.com
We use a LoftPro Gutter inspection Cam to view your gutters first to see if they need doing.
Window cleaning ; Professional window cleaning services, what we offer, water fed pole window cleaning able to reach windows up to 60 feet.
Conservatory cleaning.
Conservatory roof cleaning.
Fascias & Soffits cleaning.
Excellent Customer Service.
Target Market(s)
domestic houses
Industry/Entity Type
window cleaning
Look and feel
Each slider illustrates characteristics of the customer's brand and the style your logo design should communicate.

```html
<!DOCTYPE html>
<html lang="en">
<head>
<meta charset="utf-8">
<title>Window and Gutter Cleaning Flyer</title>
<link href="https://fonts.googleapis.com/css2?family=Lato:ital,wght@0,400;0,700;0,900;1,700;1,900&display=swap" rel="stylesheet">
<style>
:root{
  --navy:#2a2a6e;
  --navy-deep:#232260;
  --blue:#2f7fd0;
  --blue-light:#6fb0e8;
  --sky:#8fb4e2;
  --grey-panel:#e7e8ec;
  --ink:#2b2b3a;
  --white:#ffffff;
  --stage:#3a3a3a;
}
*{box-sizing:border-box;margin:0;padding:0}
html,body{width:900px;height:1200px;overflow:hidden}
body{background:var(--stage);font-family:"Lato",Arial,sans-serif;position:relative}
.flyer{position:absolute;top:290px;width:420px;height:620px;background:var(--white);overflow:hidden}
.flyer--window{left:20px}
.flyer--gutter{left:460px}
.abs{position:absolute}
.placeholder{position:absolute}

/* window side */
.hero{left:0;top:0;width:420px;height:265px;background:linear-gradient(160deg,#4f9be0 0%,#2a6fc0 55%,#6fb0e8 100%)}
.headline{left:40px;top:42px;width:200px;text-align:center;color:var(--white);line-height:1}
.headline__kicker{font-size:12px;font-weight:700;font-style:italic}
.headline__main{font-size:23px;font-weight:900;margin-top:3px}
.headline__sub{font-size:11px;font-weight:700;margin-top:3px}
.brand{right:18px;top:16px;display:flex;align-items:center;gap:6px;color:var(--navy);font-size:14px;font-weight:900;letter-spacing:.5px}
.brand__mark{width:12px;height:12px;background:var(--navy)}
.person{left:38px;top:118px;width:108px;height:152px;background:linear-gradient(180deg,#7fb6e6,#3c7cc2);border-radius:4px}
.navy-band{left:0;top:188px;width:420px;height:80px;background:var(--navy);clip-path:polygon(0 14%,18% 6%,40% 12%,62% 2%,82% 10%,100% 0,100% 100%,0 100%)}
.band-copy{left:170px;top:203px;width:238px;color:var(--white)}
.band-copy h2{font-size:10px;font-weight:700;text-align:center;margin-bottom:4px}
.band-copy p{font-size:5.6px;line-height:1.42}
.window-photo{left:232px;top:268px;width:188px;height:150px;background:linear-gradient(135deg,#d9dfe6,#8ea4bb 60%,#c9d3dd)}
.benefits-bar{left:0;top:282px;width:205px;height:20px;background:var(--blue);color:var(--white);font-size:10px;font-weight:700;padding:4px 0 0 16px;clip-path:polygon(0 0,95% 0,100% 50%,95% 100%,0 100%)}
.intro{left:15px;top:310px;width:205px;font-size:6.6px;line-height:1.45;color:var(--ink)}
.benefits{left:15px;top:352px;width:200px;list-style:none}
.benefits li{display:flex;gap:6px;font-size:5.4px;line-height:1.4;color:var(--ink);margin-bottom:8px}
.benefits svg{flex:0 0 9px;height:9px}
.benefits b{font-weight:700}
.traditional{left:250px;top:418px;width:170px;height:137px;background:var(--blue);color:var(--white);padding:12px 10px}
.traditional h2{font-size:10px;font-weight:700;text-align:center;margin-bottom:6px}
.traditional p{font-size:5.4px;line-height:1.45}
.bucket{left:186px;top:500px;width:62px;height:55px;background:linear-gradient(180deg,#f2d34a,#3f86c9);border-radius:6px}
.contact-bar{left:0;top:555px;width:420px;height:36px;display:flex;align-items:center;justify-content:center;gap:12px;font-size:14px}
.contact-bar--navy{background:var(--navy);color:var(--white)}
.contact-bar--sky{background:var(--sky);color:var(--navy-deep);top:543px}
.contact-bar__rule{width:1.5px;height:22px;background:currentColor}
.website{left:0;top:595px;width:420px;text-align:center;font-size:6.5px;letter-spacing:1.6px;color:var(--ink);font-weight:700}
.legal{left:0;top:606px;width:420px;text-align:center;font-size:5.2px;color:var(--ink)}

/* gutter side */
.top-band{left:0;top:0;width:420px;height:76px;background:var(--navy)}
.top-band h1{color:var(--white);font-size:20px;font-weight:900;text-align:center;padding-top:26px;letter-spacing:.3px}
.gutter-photo{left:0;top:70px;width:420px;height:200px;background:linear-gradient(170deg,#9fb0b8 0%,#7a6a55 45%,#b89266 70%,#d8dde2 100%);clip-path:polygon(0 3%,30% 0,60% 4%,100% 1%,100% 97%,70% 100%,35% 96%,0 100%)}
.gutter-title{left:16px;top:284px;width:172px;text-align:center;line-height:1}
.gutter-title__kicker{font-size:13px;font-weight:900;color:var(--navy)}
.gutter-title__main{font-size:30px;font-weight:900;color:var(--navy);margin-top:2px}
.gutter-title__sub{font-size:12.5px;font-weight:900;color:var(--blue);margin-top:1px}
.gutter-title__note{font-size:5.8px;color:var(--ink);margin-top:3px}
.ladder-photo{left:16px;top:368px;width:172px;height:134px;background:linear-gradient(160deg,#bcd3ea,#f1f1ee 50%,#6f8fb0)}
.gutter-copy{left:195px;top:276px;width:215px}
.gutter-copy p{font-size:6.7px;line-height:1.38;color:var(--ink);padding:5px 6px;margin-bottom:3px}
.gutter-copy p:nth-child(even){background:var(--grey-panel)}
</style>
</head>
<body>

<section class="flyer flyer--window">
  <div class="placeholder hero" role="img" aria-label="Close-up of a hand wiping a soapy blue window with a squeegee"></div>
  <div class="abs headline">
    <div class="headline__kicker">High Quality, Professional</div>
    <div class="headline__main">WINDOW<br>CLEANING</div>
    <div class="headline__sub">service across west Edinburgh</div>
  </div>
  <div class="abs brand"><span class="brand__mark"></span>ClearPane Vista</div>
  <div class="abs navy-band"></div>
  <div class="placeholder person" role="img" aria-label="Cleaner in apron and gloves holding a spray bottle"></div>
  <div class="abs band-copy">
    <h2>Window cleaning</h2>
    <p>Regular window cleaning helps to avoid the build-up of dirt and residue on the glass, meaning more light can get into your home. Our water fed poles reach windows up to 60 feet. We also offer conservatory cleaning, conservatory roof cleaning and fascias &amp; soffits cleaning, all backed by excellent customer service.</p>
  </div>
  <div class="placeholder window-photo" role="img" aria-label="Window cleaner on a ladder cleaning house windows"></div>
  <div class="abs benefits-bar">Benefits of pure hot water system</div>
  <p class="abs intro">Our industry has developed a safer method of cleaning windows through the use of long reaching telescopic poles (water fed poles), allowing windows to be cleaned from the safety of the ground.</p>
  <ul class="abs benefits">
    <li><svg viewBox="0 0 10 10"><rect width="10" height="10" rx="1.5" fill="#2f7fd0"/><path d="M2.5 5.2l1.7 1.7 3.4-3.6" stroke="#fff" stroke-width="1.3" fill="none"/></svg><span><b>Better cleaning results:</b> The purified HOT water means no chemicals or detergents are required. Windows will be left wet but don't worry, they will dry naturally streak-free.</span></li>
    <li><svg viewBox="0 0 10 10"><rect width="10" height="10" rx="1.5" fill="#2f7fd0"/><path d="M2.5 5.2l1.7 1.7 3.4-3.6" stroke="#fff" stroke-width="1.3" fill="none"/></svg><span><b>Frames and sills are cleaned at the same time:</b> Cobwebs and beasties that usually hide in the corner, will now be removed!</span></li>
    <li><svg viewBox="0 0 10 10"><rect width="10" height="10" rx="1.5" fill="#2f7fd0"/><path d="M2.5 5.2l1.7 1.7 3.4-3.6" stroke="#fff" stroke-width="1.3" fill="none"/></svg><span><b>Reduced disturbance to you and your garden:</b> Although we do our best to keep disturbance to a minimum, ladder use causes some inevitable disturbance eg. rattling of the metal, dents in your lawn, etc. These problems are avoided with the use of water fed poles.</span></li>
    <li><svg viewBox="0 0 10 10"><rect width="10" height="10" rx="1.5" fill="#2f7fd0"/><path d="M2.5 5.2l1.7 1.7 3.4-3.6" stroke="#fff" stroke-width="1.3" fill="none"/></svg><span><b>Increased privacy:</b> No need to worry about the window cleaner suddenly appearing at the window!</span></li>
    <li><svg viewBox="0 0 10 10"><rect width="10" height="10" rx="1.5" fill="#2f7fd0"/><path d="M2.5 5.2l1.7 1.7 3.4-3.6" stroke="#fff" stroke-width="1.3" fill="none"/></svg><span><b>Improved access:</b> We can now reach with ease previously inaccessible aspects of your property such as third floor windows, conservatory roofs, windows above the conservatory or sloping roofs and other windows that previously had to be left for safety reasons.</span></li>
    <li><svg viewBox="0 0 10 10"><rect width="10" height="10" rx="1.5" fill="#2f7fd0"/><path d="M2.5 5.2l1.7 1.7 3.4-3.6" stroke="#fff" stroke-width="1.3" fill="none"/></svg><span>No need to move your car out the driveway!</span></li>
  </ul>
  <div class="abs traditional">
    <h2>Traditional window cleaning</h2>
    <p>Sticky tape and tough stains like paint, putty, varnish or old bird mess may need to be cleaned by hand, or detailed. Also, the windows must be cleaned regularly and even when they are, it normally takes the system two or three cleans before the windows look completely free of marks. This is because of impurities left on the glass and frames after the initial clean, or too much dirt deposited on the windows due to irregular cleaning. So, if you are looking for a one-off clean, or only like your windows cleaned twice a year, this may not be the system for you.</p>
  </div>
  <div class="placeholder bucket" role="img" aria-label="Yellow bucket with cleaning sprays and sponges"></div>
  <div class="abs contact-bar contact-bar--navy"><span>0800 315 4720</span><span class="contact-bar__rule"></span><span>info@clearpane-vista-services.com</span></div>
  <div class="abs website">www.clearpane-vista-services.com</div>
  <div class="abs legal">7 Tarnlow Brae, North Pellin, Edinburgh EH14 3RW · Licensed by Borough of Halvern Council</div>
</section>

<section class="flyer flyer--gutter">
  <div class="placeholder gutter-photo" role="img" aria-label="Roof gutter clogged with dry leaves below roof shingles"></div>
  <div class="abs top-band"><h1>GUTTER CLEANING</h1></div>
  <div class="abs gutter-title">
    <div class="gutter-title__kicker">Fast and Easy</div>
    <div class="gutter-title__main">GUTTER</div>
    <div class="gutter-title__sub">CLEANING SERVICE</div>
    <div class="gutter-title__note">on residential and commercial properties</div>
  </div>
  <div class="placeholder ladder-photo" role="img" aria-label="Worker on a ladder clearing a house gutter"></div>
  <div class="abs gutter-copy">
    <p>Gutters are an important part of your home. Letting your gutters get blocked up can cause damage to your property, so why not set up an annual plan and make sure you don't run into problems when winter comes.</p>
    <p>Over time your gutters will fill up with moss, leaves and other unwanted debris which will affect the appearance of your home. When gutters aren't cleared and emptied on a regular basis they become heavy and risk pulling away from the fascias.</p>
    <p>When gutters are not clear it can also lead to blockages in the gutters and downpipes, which will cause the water to overflow. We use a LoftPro gutter inspection cam to view your gutters first, so you know if they need doing.</p>
    <p>We recommend gutters to be cleared out once a year. If your gutters are blocked and overflowing, why not contact us for a free no obligation quote to clear them out and get them working as they should. We will clear all gutters and unblock all downpipes ensuring the water is running freely and down your drains.</p>
  </div>
  <div class="abs contact-bar contact-bar--sky"><span>0800 315 4720</span><span class="contact-bar__rule"></span><span>info@clearpane-vista-services.com</span></div>
  <div class="abs website">www.clearpane-vista-services.com</div>
  <div class="abs legal">7 Tarnlow Brae, North Pellin, Edinburgh EH14 3RW · Licensed by Borough of Halvern Council</div>
</section>

</body>
</html>
```